Copper Vale Winery wants innovative label for unique bottling

We are looking for a lable for a champagne which is made of Eiswein (Ice Wine; this is what you get when you harvest the grapes at temperatures below -7 degrees celsius. the water is frozen and you only get the pure extract out of the grapes (sugar, acid and all the aromas). even after fermentation is remains very sweet. we then turned it into champagne (2nd fermentation in bottles for another 12 months and so on and so forth). It is bottled in small champagne bottles (0,375 l). Dark green (just like a champagne bottle). The name of the product is "Glintova" (from Freeze and Riesling). So it is unique, it is sparkling, it is sweet, it is full of aromas and it is produced from deep frozen grapes. All of this hopefully creates ideas in your imagination which lead to great designs! The only word printed onto the label is "Glintova". The colour code should still be recognizable. See www.brandt-wolmer.de for our standard labels and bottles. you can also download label designs and colours. we prefer modern / fresh / light design rather than traditional, flowery, pittoresque. But please not 100 different colours or screaming colours. You may also imagine transparent labels. Up to you! Have fun!

```html
<!DOCTYPE html>
<html lang="en">
<head>
<meta charset="utf-8">
<title>Glintova – Label</title>
<link rel="stylesheet" href="https://fonts.googleapis.com/css2?family=Bodoni+Moda:opsz,wght@6..96,500&display=swap">
<style>
  :root {
    --canvas: #f7f7f7;
    --label-light: #ffffff;
    --label-shade: #dcdde0;
    --ink-blue: #1f5877;
    --peak-ice: #c9d8e0;
    --peak-mid: #3f8fb3;
    --peak-deep: #1b4e73;
  }
  html, body {
    margin: 0;
    padding: 0;
    width: 1200px;
    height: 2487px;
    overflow: hidden;
    background: var(--canvas);
  }
  .canvas {
    position: relative;
    width: 1200px;
    height: 2487px;
  }
  .label {
    position: absolute;
    left: 80px;
    top: 770px;
    width: 1040px;
    height: 940px;
  }
  .label svg {
    display: block;
    width: 100%;
    height: 100%;
  }
  .label-name {
    position: absolute;
    left: 330px;
    top: 390px;
    width: 680px;
    margin: 0;
    text-align: right;
    font-family: "Bodoni Moda", "Didot", serif;
    font-weight: 500;
    font-size: 146px;
    line-height: 1;
    letter-spacing: 1px;
    color: var(--ink-blue);
  }
</style>
</head>
<body>
  <main class="canvas">
    <section class="label">
      <svg viewBox="0 0 1040 940" xmlns="http://www.w3.org/2000/svg">
        <defs>
          <linearGradient id="label-paper" x1="0" y1="0" x2="1" y2="0">
            <stop offset="0" stop-color="var(--label-shade)"/>
            <stop offset="0.3" stop-color="var(--label-light)"/>
            <stop offset="0.75" stop-color="var(--label-light)"/>
            <stop offset="1" stop-color="var(--label-shade)"/>
          </linearGradient>
          <linearGradient id="peaks-tone" x1="0" y1="0" x2="0" y2="1">
            <stop offset="0" stop-color="var(--peak-ice)"/>
            <stop offset="0.35" stop-color="var(--peak-mid)"/>
            <stop offset="1" stop-color="var(--peak-deep)"/>
          </linearGradient>
        </defs>
        <path class="label-sheet" d="M0,20 C320,-20 720,40 1040,170 L1040,940 L0,940 Z" fill="url(#label-paper)"/>
        <rect class="mountain-band" x="0" y="560" width="1040" height="380" fill="url(#peaks-tone)" role="img" aria-label="Low-poly illustration of icy blue mountain peaks"/>
      </svg>
      <h1 class="label-name">Glintova</h1>
    </section>
  </main>
</body>
</html>
```